label design for cannabis

label template 4"x5.5" for a Massachusetts cannabis beverage product. labels will be transparent and placed on a blue (pantone 306C) bag.
https://www.fravostones.com/

Target Market(s)

cannabis customers in MA, 21+

Industry/Entity Type

cannabis consumer product

Font styles to use
Other font styles liked:
• DIN

Colors
0094D4
00A9DD
6FCCEA
C7EBF8
E9F6FB

Requirements
Must have
• label design with fravo logo, flavor (lemon, lime, plain, and coffee). 306C pantone for background and 11-0601 TCX for text. font=DINackground.
Nice to have
• tray icon, illustrated ice cubes in white (clear), yellow (lemon), green (lime) and brown (coffee)
Should not have
• no cartoonish characters

```html
<!DOCTYPE html>
<html lang="en">
<head>
<meta charset="utf-8">
<title>fravo infused ice cubes – label set</title>
<link href="https://fonts.googleapis.com/css2?family=Barlow+Condensed:wght@500;600;700&display=swap" rel="stylesheet">
<style>
  :root{
    --bag-blue:#00b4e0;
    --text-white:#fbfbf9;
    --warn-red:#e0312b;
    --clear-stroke:#ffffff;
    --clear-a:#e6f7fd; --clear-b:#7fd6f2;
    --lemon-stroke:#f4ec3c;
    --lemon-a:#e6f59a; --lemon-b:#a8d92e;
    --lime-stroke:#3cc43a;
    --lime-a:#a6ecaa; --lime-b:#3ccf3a;
    --coffee-stroke:#6b564b;
    --coffee-a:#e6e2de; --coffee-b:#8a7a70;
  }
  *{box-sizing:border-box;margin:0;padding:0}
  html,body{width:1200px;height:1200px;overflow:hidden;background:#fff}
  body{position:relative;font-family:"Barlow Condensed",sans-serif;color:var(--text-white)}
  .label{position:absolute;width:377px;height:519px;background:var(--bag-blue)}
  .label--clear{left:204px;top:61px;--stroke:var(--clear-stroke);--cube-a:var(--clear-a);--cube-b:var(--clear-b)}
  .label--lemon{left:627px;top:61px;--stroke:var(--lemon-stroke);--cube-a:var(--lemon-a);--cube-b:var(--lemon-b)}
  .label--lime{left:204px;top:627px;--stroke:var(--lime-stroke);--cube-a:var(--lime-a);--cube-b:var(--lime-b)}
  .label--coffee{left:627px;top:627px;--stroke:var(--coffee-stroke);--cube-a:var(--coffee-a);--cube-b:var(--coffee-b)}
  .brand{position:absolute;left:0;right:0;top:14px;text-align:center;font-weight:700;font-size:106px;line-height:1;letter-spacing:-1px}
  .brand sup{position:absolute;font-size:9px;font-weight:500;top:16px;margin-left:2px;letter-spacing:0}
  .tagline{position:absolute;left:0;right:0;top:114px;text-align:center;font-weight:500;font-size:30px;line-height:1}
  .cube{position:absolute;left:105px;top:165px;width:167px;height:182px;
    border-radius:38% 38% 34% 34%/28% 28% 40% 40%;
    background:radial-gradient(circle at 40% 30%,var(--cube-a),var(--cube-b));
    border:3px solid var(--stroke)}
  .tray{position:absolute;left:121px;top:364px;width:135px;height:40px}
  .tray text{font-family:"Barlow Condensed",sans-serif;font-weight:600;font-size:11px;fill:var(--text-white)}
  .flavor{position:absolute;left:0;right:0;top:402px;text-align:center;font-weight:700;font-size:33px;line-height:1}
  .dose{position:absolute;left:0;right:0;top:440px;text-align:center;font-weight:500;font-size:15px;line-height:1}
  .warn-thc{position:absolute;left:26px;top:471px;width:40px;height:40px}
  .warn-kids{position:absolute;left:83px;top:473px;width:34px;height:34px}
  .warn-thc text,.warn-kids text{font-family:"Barlow Condensed",sans-serif;font-weight:700;fill:#111}
  .color-code{position:absolute;right:26px;top:481px;font-weight:500;font-size:17px;letter-spacing:1px;line-height:1}
</style>
</head>
<body>

<section class="label label--clear">
  <div class="brand">fravo<sup>TM</sup></div>
  <div class="tagline">infused ice cubes</div>
  <div class="cube" role="img" aria-label="Illustrated clear ice cube"></div>
  <svg class="tray" viewBox="0 0 135 40"><rect x="1" y="1" width="133" height="19" fill="none" stroke="var(--stroke)" stroke-width="2"/><text x="67.5" y="14.5" text-anchor="middle">5mg per cube</text><g fill="none" stroke="var(--stroke)" stroke-width="2"><path d="M4 20 L7 38 H23 L26 20"/><path d="M29 20 L32 38 H48 L51 20"/><path d="M54 20 L57 38 H73 L76 20"/><path d="M79 20 L82 38 H98 L101 20"/><path d="M104 20 L107 38 H123 L126 20"/></g></svg>
  <div class="flavor">clear</div>
  <div class="dose">50mg per tray</div>
  <svg class="warn-thc" viewBox="0 0 40 40"><path d="M20 2 L37 30 H3 Z" fill="#fff" stroke="var(--warn-red)" stroke-width="3" stroke-linejoin="round"/><circle cx="20" cy="21" r="4" fill="#111"/><text x="20" y="39" font-size="7.5" text-anchor="middle">CONTAINS THC</text></svg>
  <svg class="warn-kids" viewBox="0 0 34 34"><path d="M10 1.5 H24 L32.5 10 V24 L24 32.5 H10 L1.5 24 V10 Z" fill="#fff" stroke="var(--warn-red)" stroke-width="2.5"/><text x="17" y="16" font-size="7" text-anchor="middle">NOT SAFE</text><text x="17" y="23" font-size="7" text-anchor="middle">FOR KIDS</text></svg>
  <div class="color-code">11-0601 TCX</div>
</section>

<section class="label label--lemon">
  <div class="brand">fravo<sup>TM</sup></div>
  <div class="tagline">infused ice cubes</div>
  <div class="cube" role="img" aria-label="Illustrated lemon-yellow ice cube"></div>
  <svg class="tray" viewBox="0 0 135 40"><rect x="1" y="1" width="133" height="19" fill="none" stroke="var(--stroke)" stroke-width="2"/><text x="67.5" y="14.5" text-anchor="middle">5mg per cube</text><g fill="none" stroke="var(--stroke)" stroke-width="2"><path d="M4 20 L7 38 H23 L26 20"/><path d="M29 20 L32 38 H48 L51 20"/><path d="M54 20 L57 38 H73 L76 20"/><path d="M79 20 L82 38 H98 L101 20"/><path d="M104 20 L107 38 H123 L126 20"/></g></svg>
  <div class="flavor">lemon</div>
  <div class="dose">50mg per tray</div>
  <svg class="warn-thc" viewBox="0 0 40 40"><path d="M20 2 L37 30 H3 Z" fill="#fff" stroke="var(--warn-red)" stroke-width="3" stroke-linejoin="round"/><circle cx="20" cy="21" r="4" fill="#111"/><text x="20" y="39" font-size="7.5" text-anchor="middle">CONTAINS THC</text></svg>
  <svg class="warn-kids" viewBox="0 0 34 34"><path d="M10 1.5 H24 L32.5 10 V24 L24 32.5 H10 L1.5 24 V10 Z" fill="#fff" stroke="var(--warn-red)" stroke-width="2.5"/><text x="17" y="16" font-size="7" text-anchor="middle">NOT SAFE</text><text x="17" y="23" font-size="7" text-anchor="middle">FOR KIDS</text></svg>
  <div class="color-code">11-0601 TCX</div>
</section>

<section class="label label--lime">
  <div class="brand">fravo<sup>TM</sup></div>
  <div class="tagline">infused ice cubes</div>
  <div class="cube" role="img" aria-label="Illustrated lime-green ice cube"></div>
  <svg class="tray" viewBox="0 0 135 40"><rect x="1" y="1" width="133" height="19" fill="none" stroke="var(--stroke)" stroke-width="2"/><text x="67.5" y="14.5" text-anchor="middle">5mg per cube</text><g fill="none" stroke="var(--stroke)" stroke-width="2"><path d="M4 20 L7 38 H23 L26 20"/><path d="M29 20 L32 38 H48 L51 20"/><path d="M54 20 L57 38 H73 L76 20"/><path d="M79 20 L82 38 H98 L101 20"/><path d="M104 20 L107 38 H123 L126 20"/></g></svg>
  <div class="flavor">lime</div>
  <div class="dose">50mg per tray</div>
  <svg class="warn-thc" viewBox="0 0 40 40"><path d="M20 2 L37 30 H3 Z" fill="#fff" stroke="var(--warn-red)" stroke-width="3" stroke-linejoin="round"/><circle cx="20" cy="21" r="4" fill="#111"/><text x="20" y="39" font-size="7.5" text-anchor="middle">CONTAINS THC</text></svg>
  <svg class="warn-kids" viewBox="0 0 34 34"><path d="M10 1.5 H24 L32.5 10 V24 L24 32.5 H10 L1.5 24 V10 Z" fill="#fff" stroke="var(--warn-red)" stroke-width="2.5"/><text x="17" y="16" font-size="7" text-anchor="middle">NOT SAFE</text><text x="17" y="23" font-size="7" text-anchor="middle">FOR KIDS</text></svg>
  <div class="color-code">11-0601 TCX</div>
</section>

<section class="label label--coffee">
  <div class="brand">fravo<sup>TM</sup></div>
  <div class="tagline">infused ice cubes</div>
  <div class="cube" role="img" aria-label="Illustrated coffee-brown ice cube"></div>
  <svg class="tray" viewBox="0 0 135 40"><rect x="1" y="1" width="133" height="19" fill="none" stroke="var(--stroke)" stroke-width="2"/><text x="67.5" y="14.5" text-anchor="middle">5mg per cube</text><g fill="none" stroke="var(--stroke)" stroke-width="2"><path d="M4 20 L7 38 H23 L26 20"/><path d="M29 20 L32 38 H48 L51 20"/><path d="M54 20 L57 38 H73 L76 20"/><path d="M79 20 L82 38 H98 L101 20"/><path d="M104 20 L107 38 H123 L126 20"/></g></svg>
  <div class="flavor">coffee</div>
  <div class="dose">50mg per tray</div>
  <svg class="warn-thc" viewBox="0 0 40 40"><path d="M20 2 L37 30 H3 Z" fill="#fff" stroke="var(--warn-red)" stroke-width="3" stroke-linejoin="round"/><circle cx="20" cy="21" r="4" fill="#111"/><text x="20" y="39" font-size="7.5" text-anchor="middle">CONTAINS THC</text></svg>
  <svg class="warn-kids" viewBox="0 0 34 34"><path d="M10 1.5 H24 L32.5 10 V24 L24 32.5 H10 L1.5 24 V10 Z" fill="#fff" stroke="var(--warn-red)" stroke-width="2.5"/><text x="17" y="16" font-size="7" text-anchor="middle">NOT SAFE</text><text x="17" y="23" font-size="7" text-anchor="middle">FOR KIDS</text></svg>
  <div class="color-code">11-0601 TCX</div>
</section>

</body>
</html>
```